We are a building company that build new homes and units we are looking for something fresh and looks good my company name is
Larkmoor Building Group Pty Ltd

Industry/Entity Type

Building

Contact Information for Business Card

Name Marco Delacruz-Fenn
Tittle: Director
Address 14 Quarrel St. Thornbury Vic 3071
Ph: 03 9612 4087
Mobile : 0400 562 938

www.larkmoorbuildinggroup.com.au
Email: sales@larkmoorbuildinggroup.com.au

```html
<!DOCTYPE html>
<html lang="en">
<head>
<meta charset="utf-8">
<title>Larkmoor Building Group – Business Card</title>
<link rel="stylesheet" href="https://fonts.googleapis.com/css2?family=Open+Sans:wght@400;600;700&display=swap">
<style>
  :root {
    --bg: #e9e7e4;
    --card: #ffffff;
    --navy: #0f4a86;
    --ink: #1b1b1b;
    --rule: #b9c6d6;
  }
  * { box-sizing: border-box; margin: 0; padding: 0; }
  html, body { width: 1200px; height: 1000px; overflow: hidden; }
  body {
    background: var(--bg);
    font-family: "Open Sans", Arial, sans-serif;
    color: var(--ink);
    position: relative;
  }
  .card {
    position: absolute;
    left: 265px;
    width: 665px;
    height: 397px;
    background: var(--card);
    border-radius: 22px;
    overflow: hidden;
    box-shadow: 0 4px 14px rgba(0,0,0,0.18);
  }
  .card--front { top: 73px; }
  .card--back { top: 533px; }

  .brand {
    position: absolute;
    left: 0; right: 0;
    display: flex;
    align-items: center;
    justify-content: center;
    gap: 16px;
  }
  .card--front .brand { top: 130px; }
  .card--back .brand { top: 150px; }
  .brand__mark {
    width: 34px; height: 34px;
    background: var(--navy);
    flex: none;
  }
  .brand__name {
    font-weight: 600;
    font-size: 34px;
    line-height: 1.1;
    color: var(--ink);
    letter-spacing: 0.5px;
  }

  .contact {
    position: absolute;
    top: 285px;
    left: 0; right: 0;
    font-size: 15.5px;
    line-height: 21px;
  }
  .contact__person {
    position: absolute;
    right: calc(665px - 308px);
    text-align: right;
  }
  .contact__name { color: var(--navy); font-weight: 700; font-size: 16.5px; }
  .contact__divider {
    position: absolute;
    left: 332px; top: 4px;
    width: 1px; height: 70px;
    background: var(--rule);
  }
  .contact__list {
    position: absolute;
    left: 358px;
    list-style: none;
  }
  .contact__list li { display: flex; align-items: center; gap: 5px; }
  .contact__list svg { width: 12px; height: 12px; fill: var(--navy); flex: none; }

  .band {
    position: absolute;
    left: 0; right: 0; bottom: 0;
    height: 22px;
    background: var(--navy);
  }
</style>
</head>
<body>
  <section class="card card--front">
    <div class="brand">
      <span class="brand__mark"></span>
      <span class="brand__name">Larkmoor Building<br>Group Pty Ltd</span>
    </div>

    <div class="contact">
      <div class="contact__person">
        <div class="contact__name">Marco Delacruz-Fenn</div>
        <div>Director</div>
        <div>14 Quarrel St. Thornbury</div>
        <div>Vic 3071</div>
      </div>
      <div class="contact__divider"></div>
      <ul class="contact__list">
        <li><svg viewBox="0 0 12 12"><path d="M3 0h6a1 1 0 0 1 1 1v10a1 1 0 0 1-1 1H3a1 1 0 0 1-1-1V1a1 1 0 0 1 1-1zm0 1.5v8h6v-8z"/></svg>03 9612 4087</li>
        <li><svg viewBox="0 0 12 12"><path d="M1 4c0-2 2-3 5-3s5 1 5 3v1H8.5V3.8h-5V5H1zM2.5 6.5 4 5h4l1.5 1.5V11h-7z"/></svg>0400 562 938</li>
        <li><svg viewBox="0 0 12 12"><path d="M0 2h12v8H0zm1 1v.4l5 3.4 5-3.4V3zm0 1.6V9h10V4.6L6 8z"/></svg>sales@larkmoorbuildinggroup.com.au</li>
        <li><svg viewBox="0 0 12 12"><circle cx="6" cy="6" r="6"/></svg>www.larkmoorbuildinggroup.com.au</li>
      </ul>
    </div>

    <div class="band"></div>
  </section>

  <section class="card card--back">
    <div class="brand">
      <span class="brand__mark"></span>
      <span class="brand__name">Larkmoor Building<br>Group Pty Ltd</span>
    </div>
  </section>
</body>
</html>
```